Kelvor Plant Services

We are a heavy diesel mechanical business with additional air con certificates, remapping engine rebuilt

Contact Information for Business Card

Company Name, Director Name, Managing Director, Contact details, email and website

Font styles to use
Serif
Script

```html
<!DOCTYPE html>
<html lang="en">
<head>
<meta charset="utf-8">
<title>Kelvor Plant Services – Business Card</title>
<link href="https://fonts.googleapis.com/css2?family=Playfair+Display:wght@400;700;800&family=Great+Vibes&display=swap" rel="stylesheet">
<style>
  :root {
    --navy: #0c0c8c;
    --navy-deep: #07076a;
    --ink: #1b1b1b;
    --paper: #ffffff;
    --silver: #d9d9de;
    --backdrop: #e6e7ea;
  }
  * { margin: 0; padding: 0; box-sizing: border-box; }
  html, body { width: 1200px; height: 900px; overflow: hidden; }
  body {
    background: var(--backdrop);
    font-family: "Playfair Display", Georgia, serif;
    display: flex;
    flex-direction: column;
    align-items: center;
    justify-content: center;
    gap: 60px;
  }
  .card {
    width: 630px;
    height: 360px;
    position: relative;
    overflow: hidden;
    box-shadow: 0 10px 30px rgba(0,0,0,.18);
  }
  .card--front { background: var(--paper); }
  .card--back {
    background: radial-gradient(ellipse at 60% 40%, var(--navy) 0%, var(--navy-deep) 100%);
    display: flex;
    align-items: center;
    justify-content: center;
  }
  .brand {
    position: absolute;
    left: 44px;
    top: 58px;
    display: flex;
    align-items: center;
    gap: 12px;
  }
  .brand__dot {
    width: 22px; height: 22px; border-radius: 50%;
    background: var(--navy);
    flex: none;
  }
  .brand__name {
    font-weight: 800;
    font-size: 28px;
    color: var(--navy);
    line-height: 1.1;
  }
  .card--back .brand { position: static; }
  .card--back .brand__dot { background: var(--silver); width: 30px; height: 30px; }
  .card--back .brand__name { color: var(--silver); font-size: 40px; }
  .person {
    position: absolute;
    right: 54px;
    top: 140px;
    text-align: right;
  }
  .person__name {
    font-weight: 800;
    font-size: 27px;
    line-height: 1.15;
    color: var(--navy);
    letter-spacing: .6px;
    text-transform: uppercase;
  }
  .person__role {
    font-family: "Great Vibes", cursive;
    font-size: 24px;
    line-height: 1.1;
    color: var(--ink);
  }
  .edge-tab {
    position: absolute;
    right: -18px;
    top: 186px;
    width: 36px; height: 36px;
    border-radius: 50%;
    background: var(--navy);
  }
  .contact {
    position: absolute;
    right: 54px;
    bottom: 30px;
    text-align: right;
    font-size: 15px;
    color: var(--ink);
    line-height: 1.4;
  }
  .contact__address { margin-bottom: 10px; }
  .contact__line { display: flex; justify-content: flex-end; align-items: center; gap: 7px; }
  .contact__line svg { width: 13px; height: 13px; flex: none; }
  .contact__domain { color: var(--navy); font-style: normal; }
</style>
</head>
<body>
  <section class="card card--front">
    <div class="brand">
      <span class="brand__dot"></span>
      <span class="brand__name">Kelvor Plant Services</span>
    </div>

    <div class="person">
      <p class="person__name">Daniel Hartley</p>
      <p class="person__role">Director</p>
    </div>
    <span class="edge-tab"></span>

    <div class="contact">
      <p class="contact__address">2716 Marlow Ridge Rd Ashford<br>Glen, GA 30094</p>
      <p class="contact__line"><span>470-555-0182</span>
        <svg viewBox="0 0 16 16"><path fill="var(--navy)" d="M4 1l3 3-2 2c1 2 3 4 5 5l2-2 3 3-2 3C7 15 1 9 1 3z"/></svg>
      </p>
      <p class="contact__line"><span>info@kelvorplant.com</span>
        <svg viewBox="0 0 16 16"><rect x="1.5" y="3.5" width="13" height="9" fill="none" stroke="var(--navy)" stroke-width="1.6"/><path d="M1.5 3.5l6.5 5 6.5-5" fill="none" stroke="var(--navy)" stroke-width="1.6"/></svg>
      </p>
      <p class="contact__line"><span>www.<em class="contact__domain">kelvorplant</em>.com</span>
        <svg viewBox="0 0 16 16"><circle cx="8" cy="8" r="6.5" fill="none" stroke="var(--navy)" stroke-width="1.5"/><ellipse cx="8" cy="8" rx="3" ry="6.5" fill="none" stroke="var(--navy)" stroke-width="1.2"/><path d="M1.5 8h13" stroke="var(--navy)" stroke-width="1.2"/></svg>
      </p>
    </div>
  </section>

  <section class="card card--back">
    <div class="brand">
      <span class="brand__dot"></span>
      <span class="brand__name">Kelvor Plant Services</span>
    </div>
  </section>
</body>
</html>
```